Premium Triple Sec liquor / spirits brand

This is a completely open opportunity to name and design a new-to-world brand and bottle label for a triple sec (orange-flavoured liqueur). It should have premium features, a modern style and is designed to be perfect for mixing into famous cocktails such as the Margarita, Cosmopolitan and Mai Tai. The industry reference for the category is Valmorine. If you don't want to create a name, please default to 'Tavorinde'.

Target Market(s)

25-45yr olds interested in making cocktails at home (male and female)

Industry/Entity Type

Spirits / Liquor

Colors
FFC000
F8CF3A
FAE287
FDF2CF
FEFAEE
F0912C
F2A743
F7CA91
FBE8D2
FDF5EE
EE7325
F08F49
F5BC92
FAE3D3
FDF4ED

Requirements
Must have
• The liquid in any bottles must be clear.

```html
<!DOCTYPE html>
<html lang="en">
<head>
<meta charset="utf-8">
<title>Tavorinde – Orange-Flavoured Liqueur Label</title>
<link rel="stylesheet" href="https://fonts.googleapis.com/css2?family=Poiret+One&family=Josefin+Sans:wght@300;400&display=swap">
<style>
  :root {
    --backdrop: #e8d7cb;
    --label-white: #fdfbf8;
    --label-red: #d42222;
    --stripe-blue: #33b3d4;
    --band-orange: #f2a61f;
    --band-orange-deep: #ee9a12;
    --wordmark-silver: #d3d6da;
    --copy-white: #fefaee;
    --copy-grey: #6b6b6b;
    --art-leaf: #2f8a4a;
    --art-citrus: #ee7325;
    --art-citrus-light: #f5bc92;
    --art-bird-gold: #f0a62a;
    --art-bird-blue: #2a9fcf;
  }
  * { margin: 0; padding: 0; box-sizing: border-box; }
  html, body {
    width: 1200px;
    height: 798px;
    overflow: hidden;
    background: var(--backdrop);
  }
  .canvas {
    position: relative;
    width: 1200px;
    height: 798px;
    background: var(--backdrop);
  }
  .label {
    position: absolute;
    left: 367px;
    top: 24px;
    width: 465px;
    height: 750px;
    background: var(--label-white);
    overflow: hidden;
    box-shadow: 0 2px 10px rgba(90, 60, 40, 0.12);
  }
  .label__art {
    position: absolute;
    inset: 0;
    width: 465px;
    height: 750px;
  }
  .label__wordmark {
    font-family: "Poiret One", "Josefin Sans", sans-serif;
    font-size: 80px;
    fill: var(--wordmark-silver);
  }
  .label__descriptor {
    position: absolute;
    left: 100px;
    top: 380px;
    width: 260px;
    text-align: center;
    font-family: "Josefin Sans", sans-serif;
    font-weight: 300;
    font-size: 17px;
    line-height: 26px;
    letter-spacing: 1.2px;
    color: var(--copy-white);
    text-transform: uppercase;
  }
  .label__volume {
    position: absolute;
    left: 180px;
    top: 700px;
    width: 100px;
    text-align: center;
    font-family: "Josefin Sans", sans-serif;
    font-weight: 300;
    font-size: 12px;
    color: var(--copy-grey);
  }
</style>
</head>
<body>
<main class="canvas">
  <section class="label" aria-label="Tavorinde bottle label">
    <svg class="label__art" viewBox="0 0 465 750" xmlns="http://www.w3.org/2000/svg">
      <defs>
        <linearGradient id="band-orange-fill" x1="0" y1="0" x2="1" y2="1">
          <stop offset="0" stop-color="var(--band-orange)"/>
          <stop offset="1" stop-color="var(--band-orange-deep)"/>
        </linearGradient>
        <linearGradient id="bird-fill" x1="0" y1="0" x2="1" y2="0">
          <stop offset="0" stop-color="var(--art-bird-gold)"/>
          <stop offset="0.65" stop-color="var(--art-bird-gold)"/>
          <stop offset="1" stop-color="var(--art-bird-blue)"/>
        </linearGradient>
      </defs>

      <polygon class="band band--orange" points="0,355 330,245 465,305 465,750 310,750 0,465" fill="url(#band-orange-fill)"/>
      <polygon class="band band--red" points="0,0 465,0 465,175 0,355" fill="var(--label-red)"/>
      <polygon class="stripe stripe--upper" points="95,125 425,-2 425,8 98,126" fill="var(--stripe-blue)"/>
      <polygon class="stripe stripe--lower" points="55,285 420,143 410,152 55,302" fill="var(--stripe-blue)"/>

      <text class="label__wordmark" x="65" y="235" transform="rotate(-22 65 235)" textLength="370" lengthAdjust="spacingAndGlyphs">TAVORINDE</text>

      <g class="art art--leaf" role="img" aria-label="Illustration of a green citrus leaf">
        <ellipse cx="18" cy="365" rx="42" ry="128" fill="var(--art-leaf)"/>
      </g>
      <g class="art art--citrus-wedge" role="img" aria-label="Illustration of orange segments">
        <path d="M330,300 Q400,240 465,200 L465,360 Q400,330 330,300 Z" fill="var(--art-citrus)"/>
      </g>
      <g class="art art--citrus-slice" role="img" aria-label="Illustration of a sliced orange">
        <circle cx="30" cy="640" r="122" fill="var(--art-citrus)"/>
        <circle cx="30" cy="640" r="108" fill="var(--art-citrus-light)" opacity="0.45"/>
      </g>
      <g class="art art--macaw" role="img" aria-label="Illustration of a blue and gold macaw">
        <path d="M265,750 L265,500 Q265,432 335,432 L395,432 Q465,432 465,500 L465,750 Z" fill="url(#bird-fill)"/>
      </g>
    </svg>

    <p class="label__descriptor">Orange-Flavoured<br>Liqueur</p>
    <p class="label__volume">700ml</p>
  </section>
</main>
</body>
</html>
```